Email Sign Up Form (Lightbox)

We are looking for a 320 X 380 graphic design to be used as a lightbox style email sign up form (if unfamiliar with what a lightbox is, please see attached designs) on our website, https://www.brightlanemotorist.net to capture email sign ups during the holiday season. The theme for this lightbox is “Gifts for Truck Drivers” and we have attached some graphics that have been used in the past to provide inspiration.

The following text and elements must be included on the design:

Headline – 2014’s Hottest Holiday Gifts for Truckers

Supporting text– Get Free Trucker Gift Guide!

Required form field – Email address

Graphic Button CTA – Give Me Gift Ideas!

We want to keep this text simple and easy to read while using strong graphics to really grab our site visitors’ attention and prompt them to sign up to receive our gift guide emails. The users of this guide are searching for gift ideas for the truck drivers on their list. This lightbox should entice them to join our mailing list for great, relevant gift suggestions. Though this website is about trucking, it should not look overtly trucking - it should have a Christmas holiday feel.

Once a lightbox design has been approved, the winner will need to provide us with a layered .psd file so we can effectively implement the design. To help illustrate what some of our current lightboxes look like, we have included some screen shots in the attachment area. We feel our current lightboxes are too text driven and basic in design. We are looking for something new and fresh that really stands out while being complimentary to our website.

The target markets for this design are truck drivers as well as friends/family of truck drivers.

Industry/Entity Type

Graphic Design

Font styles to use
Sans Serif

Colors
eb2027
3176b5
00a88f
fbee3e

Requirements
Must have
• A Christmas/holiday themed background in using traditional color associated with Christmas designs (gradients are fine).

```html
<!DOCTYPE html>
<html lang="en">
<head>
<meta charset="utf-8">
<title>Holiday Gifts for Truckers – Sign Up</title>
<link rel="stylesheet" href="https://fonts.googleapis.com/css2?family=Open+Sans:wght@400;600;700&family=Titan+One&family=Pacifico&display=swap">
<style>
  :root {
    --stage: #2f3432;
    --green-deep: #0e5c18;
    --green-mid: #1f8a25;
    --green-light: #3fae2e;
    --ribbon-blue: #1c6db8;
    --ribbon-dark: #0f4f8f;
    --ribbon-stitch: #ffffff;
    --text-white: #ffffff;
    --field-border: #f08a1c;
    --field-text: #3a5a2a;
    --button-blue: #1463a8;
    --button-edge: #4fb0ea;
  }
  * { box-sizing: border-box; margin: 0; padding: 0; }
  html, body { width: 1200px; height: 800px; overflow: hidden; }
  body { background: var(--stage); position: relative; font-family: "Open Sans", Arial, sans-serif; }

  .signup-lightbox { position: absolute; left: 438px; top: 190px; width: 320px; height: 372px; }

  .lightbox-panel {
    position: absolute; left: 0; top: 63px; width: 320px; height: 296px;
    background: radial-gradient(ellipse at 50% 45%, var(--green-light) 0%, var(--green-mid) 45%, var(--green-deep) 100%);
  }

  .gift-illustration {
    position: absolute; left: 4px; top: 92px; width: 312px; height: 148px;
    background: radial-gradient(ellipse at 60% 50%, #e7e3d6 0%, #c9c2ae 35%, rgba(60,140,50,0) 75%);
  }

  .title-ribbon { position: absolute; left: 0; top: 0; width: 320px; height: 104px; }
  .ribbon-text { position: absolute; left: 0; width: 320px; text-align: center; color: var(--text-white); }
  .ribbon-year { top: 6px; font-family: "Pacifico", cursive; font-size: 15px; line-height: 20px; }
  .ribbon-main { top: 28px; font-family: "Titan One", sans-serif; font-size: 25px; line-height: 30px; letter-spacing: 0.3px; text-shadow: 0 2px 0 var(--ribbon-dark); }
  .ribbon-sub { top: 58px; font-family: "Titan One", sans-serif; font-size: 12px; line-height: 16px; letter-spacing: 1.2px; }

  .supporting-text {
    position: absolute; left: 0; top: 247px; width: 320px; text-align: center;
    color: var(--text-white); font-weight: 600; font-size: 18.5px; line-height: 24px;
  }

  .email-field {
    position: absolute; left: 40px; top: 281px; width: 237px; height: 39px;
    background: #fff; border: 1.5px dashed var(--field-border);
    padding: 0 11px; display: flex; align-items: center;
    font-size: 13px; color: var(--field-text);
  }

  .cta-button {
    position: absolute; left: 65px; top: 338px; width: 178px; height: 31px;
    background: linear-gradient(#1b74bf, var(--button-blue));
    border: 2px solid var(--button-edge);
    display: flex; align-items: center; justify-content: center; gap: 8px;
    color: var(--text-white); font-weight: 700; font-size: 12.5px;
  }
</style>
</head>
<body>
  <div class="signup-lightbox">
    <div class="lightbox-panel"></div>
    <div class="gift-illustration" role="img" aria-label="Illustration of a trucker gift checklist clipboard beside three wrapped presents with red, yellow and blue bows"></div>

    <svg class="title-ribbon" viewBox="0 0 320 104" aria-hidden="true">
      <polygon points="2,30 34,30 34,100 2,100 12,65" fill="var(--ribbon-dark)"/>
      <polygon points="318,30 286,30 286,100 318,100 308,65" fill="var(--ribbon-dark)"/>
      <polygon points="28,90 34,100 34,90" fill="#0a3a6a"/>
      <polygon points="292,90 286,100 286,90" fill="#0a3a6a"/>
      <path d="M30 0 H290 V86 L160 92 L30 86 Z" fill="var(--ribbon-blue)"/>
      <path d="M36 5 H284 V81 L160 87 L36 81 Z" fill="none" stroke="var(--ribbon-stitch)" stroke-width="1.3" stroke-dasharray="5 3"/>
    </svg>
    <div class="ribbon-text ribbon-year">2014’s Hottest</div>
    <div class="ribbon-text ribbon-main">Holiday Gifts</div>
    <div class="ribbon-text ribbon-sub">FOR TRUCKERS</div>

    <p class="supporting-text">Get Free Trucker Gift Guide!</p>
    <div class="email-field">Email address</div>
    <div class="cta-button">
      <span>Give Me Gift Ideas!</span>
      <svg width="8" height="11" viewBox="0 0 8 11" aria-hidden="true"><path d="M1.5 1 L6 5.5 L1.5 10" fill="none" stroke="#fff" stroke-width="2.2"/></svg>
    </div>
  </div>
</body>
</html>
```